Briar Vale personal care products line

I need a label design for a line of shampoo, conditioner, beard oil, body butter, massage oil, all containing Hemp oil, All Natural product. No phosphates,
I want the design to feel unisex but want to keep it clean as possible. This is for upscale salons and needs to say on the label professional styling products on the label. Please visit my facebook page www.facebook.com/briarvale to see the description of the product benefits. I am attaching some ideas I like as well as the briar vale logo. I would like to see any color of bottle you best think will suit this product as well as new logo design. I am not set on any of these elements. Just the name Briar Vale.

Project Deadline Extended Reason: I have extended the deadline as I had not filled out the description for the design as it should be. I have also added some features that will define the idea as to what we need. I am open to any desing using Briar Vale. The tag line is not anything I am determined to keep either. Please just be creative and help come up with a great product label for this name and product.Thank you to all ! Added Tuesday, June 2, 2015

Target Market(s)

Salons and upper end market

Industry/Entity Type

Cosmetology

Font styles to use
Serif
Sans Serif

Requirements
Must have
• Logo
Nice to have
• Bottle and packaging ideas on color and shape of bottle

```html
<!DOCTYPE html>
<html lang="en">
<head>
<meta charset="utf-8">
<title>Briar Vale – Hair &amp; Scalp Label</title>
<link rel="stylesheet" href="https://fonts.googleapis.com/css2?family=Francois+One&family=Caveat:wght@500&family=Kaushan+Script&display=swap">
<style>
  :root {
    --forest: #1f5128;
    --mint: #a3f5ad;
    --leaf: #35a844;
    --ink-green: #2e6b3a;
    --ink: #1c1c1c;
    --paper: #ffffff;
    --backdrop: #ffffff;
  }
  * { margin: 0; padding: 0; box-sizing: border-box; }
  html, body {
    width: 1200px;
    height: 1000px;
    overflow: hidden;
    background: var(--backdrop);
  }
  .canvas {
    position: relative;
    width: 1200px;
    height: 1000px;
  }
  .label {
    position: absolute;
    left: 180px;
    top: 250px;
    width: 840px;
    height: 472px;
    background: var(--paper);
    box-shadow: 0 12px 40px rgba(0,0,0,0.45);
    overflow: hidden;
  }
  .band { position: absolute; left: 0; width: 100%; }
  .band-top-dark { top: 0; height: 57px; background: var(--forest); }
  .band-top-light { top: 57px; height: 50px; background: var(--mint); }
  .band-bottom-light { top: 437px; height: 18px; background: var(--mint); }
  .band-bottom-dark { top: 455px; height: 17px; background: var(--forest); }

  .brand-mark {
    position: absolute;
    left: 50%;
    top: 40px;
    transform: translateX(-50%);
    width: 150px;
    height: 150px;
  }
  .brand-name {
    position: absolute;
    left: 0;
    width: 100%;
    top: 196px;
    text-align: center;
    font-family: "Francois One", sans-serif;
    font-size: 52px;
    line-height: 1;
    color: var(--leaf);
  }
  .tagline {
    position: absolute;
    left: 0;
    width: 100%;
    top: 260px;
    text-align: center;
    font-family: "Caveat", cursive;
    font-size: 34px;
    line-height: 1;
    color: var(--ink);
  }
  .benefits {
    position: absolute;
    left: 0;
    width: 100%;
    top: 318px;
    text-align: center;
    font-family: "Kaushan Script", cursive;
    font-size: 26px;
    line-height: 34px;
    color: var(--ink-green);
  }
</style>
</head>
<body>
  <main class="canvas">
    <section class="label" aria-label="Briar Vale hair and scalp product label">
      <div class="band band-top-dark"></div>
      <div class="band band-top-light"></div>

      <svg class="brand-mark" viewBox="0 0 150 150" aria-hidden="true">
        <circle cx="75" cy="75" r="70" fill="var(--paper)"/>
        <circle cx="75" cy="75" r="58" fill="var(--leaf)"/>
      </svg>

      <h1 class="brand-name">Briar Vale</h1>
      <p class="tagline">Let it grow from the Vale!</p>
      <p class="benefits">
        100% Natural Hair &amp; Scalp<br>
        Nourishment with Acedic Acid<br>
        &amp; Hemp Omega 3 Oils
      </p>

      <div class="band band-bottom-light"></div>
      <div class="band band-bottom-dark"></div>
    </section>
  </main>
</body>
</html>
```